WEBSITE DESIGN - www.brindolux.com

We need a professional and modern looking website for our business. The current website was only made tentatively and can be viewed (we expect a website MUCH better than this). It needs to be simple and non-cluttered yet look modern and sophisticated. It needs to be very easy to navigate as our tarket market is people over the age of 45. Our logo is attached below and this should be incorporated plus the colours/theme should match this. We don't mind purchasing images online if your design includes these and we like it.

Any other specific questions please enquire as we want to hear them.

Target Market(s)

over 45 age english speaking westerners

Industry/Entity Type

Business

Number of Pages Required

1 page

Requirements
Must have
• -our logo (attached).
• -page tabs as those described (tabs.. but not necessarily each of these pages completed as well although this would be nice).
• -social media logos
• Pages should include: homepage, services, pricing, about us, contact us. There should also be a payments page designed which would link with the other pages but there would be no tab for this.

```html
<!DOCTYPE html>
<html lang="en">
<head>
<meta charset="utf-8">
<title>Brindolux Computer Solutions</title>
<link href="https://fonts.googleapis.com/css2?family=Open+Sans:wght@300;400;600;700&display=swap" rel="stylesheet">
<style>
:root{
  --orange:#c98106;
  --orange-dark:#b06f00;
  --ink:#333333;
  --muted:#777777;
  --light:#f1f1f1;
  --panel:#e4e4e4;
  --dark:#2a2a2a;
  --darker:#1e1e1e;
  --white:#ffffff;
}
*{box-sizing:border-box;margin:0;padding:0}
html,body{width:1200px;height:5000px;overflow:hidden}
body{font-family:'Open Sans',Arial,sans-serif;color:var(--ink);background:var(--white);font-size:15px}
section,header,footer{position:relative;width:1200px}
.section-title{font-size:30px;font-weight:400;color:var(--ink);text-align:center}
.divider{display:flex;align-items:center;justify-content:center;gap:8px;margin:14px auto}
.divider span{display:block;width:60px;height:1px;background:#bbb}
.divider i{display:block;width:7px;height:7px;border-radius:50%;background:var(--orange)}
.subtitle{font-size:13px;color:var(--muted);text-align:center}

/* header */
.site-header{height:100px;display:flex;align-items:center;justify-content:space-between;padding:0 100px}
.brand{display:flex;align-items:center;gap:12px;font-size:30px;font-weight:400;color:var(--ink)}
.brand .mark{width:32px;height:32px;border-radius:50%;background:var(--orange)}
.brand small{display:block;font-size:10px;letter-spacing:2px;color:var(--muted)}
.main-nav{display:flex;gap:38px;font-size:14px;text-transform:uppercase}
.main-nav a{color:var(--ink);text-decoration:none;padding-bottom:8px}
.main-nav a.active{color:var(--orange);border-bottom:2px solid var(--orange)}

/* hero */
.hero{height:565px;overflow:hidden}
.hero-photo{position:absolute;inset:0;background:linear-gradient(100deg,#4a4a46 0%,#8a847a 40%,#b7b0a2 60%,#5f5a52 100%)}
.hero-copy{position:absolute;left:100px;top:150px;color:var(--white)}
.hero-copy h1{font-size:42px;font-weight:700}
.hero-copy p{font-size:22px;margin-top:6px}
.hero-arrow{position:absolute;top:220px}
.hero-arrow.left{left:22px}.hero-arrow.right{right:22px}
.hero-contact{position:absolute;left:0;right:0;bottom:22px;height:36px;background:rgba(30,30,30,.75);display:flex;justify-content:center;align-items:center;gap:30px;color:var(--white);font-size:13px}
.hero-contact b{color:var(--orange);font-weight:600}

/* intro */
.intro{height:278px;padding-top:75px}
.intro p{width:960px;margin:0 auto;text-align:center;font-size:13px;line-height:22px;color:var(--muted)}

/* trust */
.trust{height:424px;background:var(--orange);padding-top:45px}
.trust .section-title{color:#3a2500}
.trust .divider span{background:#e8b45a}.trust .divider i{background:var(--white)}
.trust-stats{display:flex;justify-content:center;gap:70px;margin-top:60px}
.stat{width:120px;height:120px;position:relative;color:var(--white);text-align:center}
.stat::before{content:"";position:absolute;inset:12px;border:2px solid rgba(255,255,255,.55);transform:rotate(45deg);background:rgba(255,255,255,.08)}
.stat-inner{position:relative;padding-top:22px}
.stat svg{display:block;margin:0 auto}
.stat strong{display:block;font-size:30px;font-weight:400;line-height:34px}
.stat span{font-size:12px}

/* why */
.why{height:500px;padding-top:75px}
.why .lead{font-size:13px;color:var(--ink);text-align:center}
.why-grid{display:flex;justify-content:center;gap:26px;margin-top:40px}
.why-item{width:240px;text-align:center}
.why-item .thumb{height:88px;border-radius:2px}
.why-item h3{font-size:15px;font-weight:700;margin:16px 0 8px;text-transform:uppercase}
.why-item p{font-size:12.5px;line-height:18px;color:var(--muted)}

/* skills */
.skills{height:360px;margin-top:40px;background:linear-gradient(180deg,#3a3a3a,#262626);display:flex;justify-content:center;gap:52px;padding-top:80px}
.skill{width:140px;text-align:center;color:var(--white)}
.skill h4{font-size:12.5px;font-weight:600;height:40px;display:flex;align-items:flex-end;justify-content:center;text-transform:uppercase}
.skill .ring{position:relative;width:136px;height:136px;margin:10px auto 0}
.skill .ring b{position:absolute;inset:0;display:flex;align-items:center;justify-content:center;font-size:28px;font-weight:400}

/* services */
.services{height:573px;padding-top:60px}
.service-grid{display:flex;justify-content:center;gap:28px;margin-top:45px}
.service{width:230px;height:300px;background:var(--panel);text-align:center;padding-top:30px}
.service.featured{background:var(--orange);color:var(--white)}
.service .icon{width:80px;height:80px;border-radius:50%;background:var(--dark);margin:0 auto;display:flex;align-items:center;justify-content:center}
.service.featured .icon{background:var(--white)}
.service h3{font-size:17px;font-weight:400;margin:22px 18px 14px;text-transform:uppercase}
.service p{font-size:14px;line-height:20px;padding:0 22px}

/* testimonial */
.testimonial{height:387px;overflow:hidden}
.testimonial-photo{position:absolute;inset:0;background:linear-gradient(90deg,#3d3d3d,#5e5e5e 50%,#3a3a3a)}
.testimonial-body{position:relative;text-align:center;color:var(--white);padding-top:60px}
.quote-badge{width:64px;height:64px;margin:0 auto;background:var(--orange);transform:rotate(45deg);display:flex;align-items:center;justify-content:center}
.quote-badge svg{transform:rotate(-45deg)}
.testimonial h2{font-size:30px;font-weight:400;margin-top:30px}
.testimonial p{width:860px;margin:14px auto 0;font-size:13px;line-height:20px}
.testimonial .who{font-size:13px;margin-top:12px}
.testimonial .who a{color:var(--orange);display:block;font-size:12px;text-decoration:none}
.dots{display:flex;justify-content:center;gap:8px;margin-top:16px}
.dots i{width:9px;height:9px;border-radius:50%;background:#999}.dots i.on{background:var(--white)}

/* pricing */
.pricing{height:866px;background:var(--light);padding-top:55px}
.plans{display:flex;justify-content:center;gap:40px;margin-top:45px}
.plan{width:320px;height:600px;background:var(--white);border:1px solid #ddd;text-align:center;padding:30px 22px}
.plan.featured{background:var(--orange);color:var(--white);border-color:var(--orange)}
.plan h3{font-size:46px;font-weight:300;color:var(--orange)}
.plan.featured h3{color:var(--white)}
.plan .prices{font-size:17px;margin-top:20px;white-space:nowrap}
.plan .prices sup{font-size:10px}
.plan .term{font-style:italic;font-size:16px;color:var(--muted);margin-top:12px}
.plan.featured .term{color:#ffe7bd}
.plan .fine{font-size:12.5px;line-height:19px;margin-top:8px}
.plan ul{list-style:none;margin-top:22px;font-size:14px}
.plan li{padding:11px 0;border-bottom:1px solid #ddd}
.plan.featured li{border-color:rgba(255,255,255,.35)}
.plan .agree{display:flex;align-items:center;justify-content:center;gap:8px;font-size:12.5px;margin-top:14px}
.plan .agree i{width:14px;height:14px;border:1px solid currentColor}
.plan .order{display:inline-block;margin-top:22px;background:var(--darker);color:var(--white);font-size:13px;font-weight:700;padding:10px 24px}
.plan.featured .order{background:var(--white);color:var(--ink)}

/* map */
.map{height:340px}
.map-fill{position:absolute;inset:0;background:linear-gradient(135deg,#b9d3e6,#e6e2d6 45%,#cfe0ea 70%,#e9e5da)}
.map-card{position:absolute;left:470px;top:75px;width:270px;height:56px;background:var(--white);box-shadow:0 2px 6px rgba(0,0,0,.25);font-size:15px;padding:14px 16px}
.map-pin{position:absolute;left:592px;top:148px}

/* cta */
.cta{height:100px;background:var(--orange);display:flex;align-items:center;justify-content:space-between;padding:0 100px}
.cta p{font-size:28px;color:#2a1800}
.cta a{background:var(--white);color:var(--ink);font-size:14px;font-weight:700;padding:12px 30px;text-decoration:none}

/* footer */
.site-footer{height:467px;background:var(--darker);color:#bbb;padding:40px 100px 0;font-size:12.5px}
.footer-main{display:flex;justify-content:space-between}
.footer-info{width:560px;display:grid;grid-template-columns:210px 300px;column-gap:40px;row-gap:26px}
.footer-col h4{color:var(--white);font-size:14px;font-weight:600;margin-bottom:10px;text-transform:uppercase}
.footer-col p,.footer-col li{line-height:19px;list-style:none}
.footer-col .accent{color:var(--orange)}
.signup{width:420px;display:grid;grid-template-columns:1fr 1fr;gap:6px;align-content:start}
.signup span{display:block;height:38px;background:#2d2d2d;border:1px solid #3a3a3a;padding:10px 12px;color:#999;font-size:11.5px}
.signup .wide{grid-column:span 2}
.signup .msg{grid-column:span 2;height:100px}
.signup .note{background:none;border:none;height:auto;padding:8px 0;color:#888;font-size:11px}
.signup .reg{justify-self:end;width:120px;background:var(--orange);color:var(--ink);text-align:center;font-weight:700;border:none;margin-top:6px}
.footer-base{grid-column:span 2}
.copyright{font-size:11px;color:#888}
.cards{display:flex;gap:8px;margin-top:10px}
.cards i{width:42px;height:26px;background:#55606a;border-radius:3px}
.cards i:nth-child(2){background:#8a6a3a}.cards i:nth-child(3){background:#7a4444}.cards i:nth-child(4){background:#4d6a4d}
</style>
</head>
<body>

<header class="site-header">
  <div class="brand"><span class="mark"></span><div>Brindolux<small>COMPUTER SOLUTIONS</small></div></div>
  <nav class="main-nav">
    <a class="active" href="#">Home</a><a href="#">Services</a><a href="#">Pricing</a><a href="#">About Us</a><a href="#">Contact Us</a>
  </nav>
</header>

<section class="hero">
  <div class="hero-photo" role="img" aria-label="Photo of a smiling man in glasses using a tablet"></div>
  <div class="hero-copy"><h1>Instant Support</h1><p>Instant Technical Help For Your Devices.</p></div>
  <svg class="hero-arrow left" width="24" height="40" viewBox="0 0 24 40"><path d="M20 4 L5 20 L20 36" fill="none" stroke="#fff" stroke-width="4"/></svg>
  <svg class="hero-arrow right" width="24" height="40" viewBox="0 0 24 40"><path d="M4 4 L19 20 L4 36" fill="none" stroke="#fff" stroke-width="4"/></svg>
  <div class="hero-contact"><span><b>USA</b> +1 555 014 2270</span><span><b>UK</b> +44 20 7946 0318</span><span><b>AU</b> +61 2 5550 1946</span></div>
</section>

<section class="intro">
  <h2 class="section-title">Our Customer Our Priority Lets Say Hi..</h2>
  <div class="divider"><span></span><i></i><span></span></div>
  <p>Brindolux was established to provide consumers with access to the sophisticated, enterprise-level IT services, support and the benefits and cost savings available to larger organisations. We provide proactive monitoring and management of computers across the country. Brindolux is a growing organisation dedicated to making your PC tech support easy and accessible.</p>
</section>

<section class="trust">
  <h2 class="section-title">We Build the Trust</h2>
  <div class="divider"><span></span><i></i><span></span></div>
  <div class="trust-stats">
    <div class="stat"><div class="stat-inner"><svg width="22" height="16" viewBox="0 0 22 16"><rect x="3" y="1" width="16" height="11" fill="none" stroke="#fff" stroke-width="1.5"/><path d="M0 15h22" stroke="#fff" stroke-width="2"/></svg><strong>986</strong><span>Laptops</span></div></div>
    <div class="stat"><div class="stat-inner"><svg width="22" height="16" viewBox="0 0 22 16"><rect x="1" y="8" width="20" height="7" fill="none" stroke="#fff" stroke-width="1.5"/><path d="M6 8V1M16 8V1" stroke="#fff" stroke-width="1.5"/></svg><strong>256</strong><span>Routers</span></div></div>
    <div class="stat"><div class="stat-inner"><svg width="22" height="16" viewBox="0 0 22 16"><rect x="7" y="0" width="9" height="16" rx="1.5" fill="none" stroke="#fff" stroke-width="1.5"/></svg><strong>867</strong><span>Phones</span></div></div>
    <div class="stat"><div class="stat-inner"><svg width="22" height="16" viewBox="0 0 22 16"><rect x="1" y="1" width="20" height="11" fill="none" stroke="#fff" stroke-width="1.5"/><path d="M7 15h8M11 12v3" stroke="#fff" stroke-width="1.5"/></svg><strong>1904</strong><span>Desktops</span></div></div>
    <div class="stat"><div class="stat-inner"><svg width="22" height="16" viewBox="0 0 22 16"><rect x="4" y="0" width="14" height="16" rx="1.5" fill="none" stroke="#fff" stroke-width="1.5"/></svg><strong>511</strong><span>Tablets</span></div></div>
    <div class="stat"><div class="stat-inner"><svg width="22" height="16" viewBox="0 0 22 16"><circle cx="11" cy="8" r="6" fill="none" stroke="#fff" stroke-width="1.5"/><circle cx="11" cy="8" r="2" fill="#fff"/></svg><strong>2456</strong><span>Software</span></div></div>
  </div>
</section>

<section class="why">
  <h2 class="section-title">Why We Are The Best</h2>
  <div class="divider"><span></span><i></i><span></span></div>
  <p class="lead">Why We Are The Best The one stop comprehensive diagnostic &amp; repair station for your computer and connected devices.We'll fix anything!</p>
  <div class="why-grid">
    <div class="why-item"><div class="thumb" role="img" aria-label="Photo of computer repair tools" style="background:linear-gradient(90deg,#6b6a52,#9a8a5c)"></div><h3>Diagnosis &amp; Repair</h3><p>The one stop comprehensive diagnostic &amp; repair station for your computer and connected devices. We'll fix anything!</p></div>
    <div class="why-item"><div class="thumb" role="img" aria-label="Photo of a new computer being set up" style="background:linear-gradient(90deg,#2f3a44,#5b6e7c)"></div><h3>Setup &amp; Install</h3><p>Confused and frustrated with device setup &amp; installation? Leave it to the experts, which means all you do is sit back and relax.</p></div>
    <div class="why-item"><div class="thumb" role="img" aria-label="Photo of an optimization keyboard key" style="background:linear-gradient(90deg,#3c3c3c,#8a7a5a)"></div><h3>Optimization</h3><p>You won't believe it's the same old computer. Your system will work like it did on the day you bought it. Anytime, anywhere remote tech help for your home devices.</p></div>
    <div class="why-item"><div class="thumb" role="img" aria-label="Illustration of a web designer at work" style="background:linear-gradient(90deg,#3e6f8e,#8fb86a)"></div><h3>Web Designing</h3><p>We develop the website, we analyse, strategize and assess our client's specific need, requirement, preference and approach. We not only create website, we create a Brand.</p></div>
  </div>
</section>

<section class="skills">
  <div class="skill"><h4>Awesomeness</h4><div class="ring"><svg width="136" height="136"><circle cx="68" cy="68" r="60" fill="none" stroke="#555" stroke-width="7"/><circle cx="68" cy="68" r="60" fill="none" stroke="#c98106" stroke-width="7" stroke-dasharray="358 377" transform="rotate(-90 68 68)"/></svg><b>95%</b></div></div>
  <div class="skill"><h4>Flexibility</h4><div class="ring"><svg width="136" height="136"><circle cx="68" cy="68" r="60" fill="none" stroke="#555" stroke-width="7"/><circle cx="68" cy="68" r="60" fill="none" stroke="#c98106" stroke-width="7" stroke-dasharray="369 377" transform="rotate(-90 68 68)"/></svg><b>98%</b></div></div>
  <div class="skill"><h4>Virus Removal</h4><div class="ring"><svg width="136" height="136"><circle cx="68" cy="68" r="60" fill="none" stroke="#555" stroke-width="7"/><circle cx="68" cy="68" r="60" fill="none" stroke="#c98106" stroke-width="7" stroke-dasharray="351 377" transform="rotate(-90 68 68)"/></svg><b>93%</b></div></div>
  <div class="skill"><h4>Support</h4><div class="ring"><svg width="136" height="136"><circle cx="68" cy="68" r="60" fill="none" stroke="#c98106" stroke-width="7"/></svg><b>100%</b></div></div>
  <div class="skill"><h4>Software Installation</h4><div class="ring"><svg width="136" height="136"><circle cx="68" cy="68" r="60" fill="none" stroke="#555" stroke-width="7"/><circle cx="68" cy="68" r="60" fill="none" stroke="#c98106" stroke-width="7" stroke-dasharray="366 377" transform="rotate(-90 68 68)"/></svg><b>97%</b></div></div>
  <div class="skill"><h4>System Setup</h4><div class="ring"><svg width="136" height="136"><circle cx="68" cy="68" r="60" fill="none" stroke="#555" stroke-width="7"/><circle cx="68" cy="68" r="60" fill="none" stroke="#c98106" stroke-width="7" stroke-dasharray="343 377" transform="rotate(-90 68 68)"/></svg><b>91%</b></div></div>
</section>

<section class="services">
  <h2 class="section-title">Best Services</h2>
  <div class="divider"><span></span><i></i><span></span></div>
  <p class="subtitle">That's What We Do</p>
  <div class="service-grid">
    <div class="service"><div class="icon"><svg width="34" height="34" viewBox="0 0 34 34"><circle cx="17" cy="17" r="9" fill="none" stroke="#fff" stroke-width="4" stroke-dasharray="5 3"/><circle cx="17" cy="17" r="3" fill="#fff"/></svg></div><h3>Tech Support</h3><p>We make technology easier for you with instant support.</p></div>
    <div class="service featured"><div class="icon"><svg width="34" height="34" viewBox="0 0 34 34"><path d="M17 4v16M10 13l7 7 7-7" fill="none" stroke="#2a2a2a" stroke-width="3"/><path d="M5 22v7h24v-7" fill="none" stroke="#2a2a2a" stroke-width="3"/></svg></div><h3>Downloads</h3><p>The best apps to optimize &amp; secure your digital devices.</p></div>
    <div class="service"><div class="icon"><svg width="34" height="34" viewBox="0 0 34 34"><rect x="4" y="6" width="26" height="17" fill="none" stroke="#fff" stroke-width="2.5"/><path d="M12 29h10M17 23v6" stroke="#fff" stroke-width="2.5"/></svg></div><h3>Web Design</h3><p>We make technology easier for you with instant support.</p></div>
    <div class="service"><div class="icon"><svg width="34" height="34" viewBox="0 0 34 34"><path d="M17 4l12 6v14l-12 6-12-6V10z" fill="none" stroke="#fff" stroke-width="2.5"/><path d="M17 11v8M13 15l4 4 4-4" fill="none" stroke="#fff" stroke-width="2.5"/></svg></div><h3>Understand the Urgency</h3><p>We make technology easier for you with instant support.</p></div>
  </div>
</section>

<section class="testimonial">
  <div class="testimonial-photo" role="img" aria-label="Dimmed photo collage of happy customers"></div>
  <div class="testimonial-body">
    <div class="quote-badge"><svg width="26" height="22" viewBox="0 0 26 22"><path d="M2 20V11Q2 3 10 2v4Q6 7 6 11h4v9zM15 20V11Q15 3 23 2v4Q19 7 19 11h4v9z" fill="#fff"/></svg></div>
    <h2>10,000+ user,who love us</h2>
    <p>Lorem ipsum is that it has a more-or-less normal distribution of letters, as opposed to using content here making it look like readable English. Many desktop publishing packages and web page editors now use.</p>
    <div class="who">Marlon Hale<a href="#">www.brindolux.com</a></div>
    <div class="dots"><i class="on"></i><i></i><i></i></div>
  </div>
</section>

<section class="pricing">
  <h2 class="section-title">Plan &amp; Pricing</h2>
  <div class="divider"><span></span><i></i><span></span></div>
  <p class="subtitle">Our Affordable Prices</p>
  <div class="plans">
    <div class="plan"><h3>Quick Fix</h3><div class="prices">NZD 95 &nbsp; USD 60<sup>*</sup> &nbsp; GBP 40<sup>*</sup></div><div class="term">1 Month</div><p class="fine">*The price advertised might not be the same price charged to the credit card account due to exchange rate fluctuations.This means that because we are based in New Zealand we have to convert your purchase to New Zealand dollars at the exchange rate on the day it is processed.</p><ul><li>1 Month Tech Support</li><li>For 1 Computer</li><li>24/7 Availability</li></ul><div class="agree"><i></i>I agree to the Terms and Conditions</div><span class="order">ORDER NOW</span></div>
    <div class="plan featured"><h3>Starter</h3><div class="prices">NZD 140 &nbsp; USD 90<sup>*</sup> &nbsp; GBP 60<sup>*</sup></div><div class="term">6 Month</div><p class="fine">*The price advertised might not be the same price charged to the credit card account due to exchange rate fluctuations.This means that because we are based in New Zealand we have to convert your purchase to New Zealand dollars at the exchange rate on the day it is processed.</p><ul><li>6 Month Tech Support</li><li>6 Month support for the same issue</li><li>24/7 Availability</li></ul><div class="agree"><i></i>I agree to the Terms and Conditions</div><span class="order">ORDER NOW</span></div>
    <div class="plan"><h3>Advance</h3><div class="prices">NZD 250 &nbsp; USD 160<sup>*</sup> &nbsp; GBP 105<sup>*</sup></div><div class="term">1 Year</div><p class="fine">*The price advertised might not be the same price charged to the credit card account due to exchange rate fluctuations.This means that because we are based in New Zealand we have to convert your purchase to New Zealand dollars at the exchange rate on the day it is processed.</p><ul><li>1 Year Tech Support</li><li>Upto 3 Computers &amp; Printers</li><li>Connected Devices with Router</li></ul><div class="agree"><i></i>I agree to the Terms and Conditions</div><span class="order">ORDER NOW</span></div>
  </div>
</section>

<section class="map">
  <div class="map-fill" role="img" aria-label="Street map showing the office location by the harbour"></div>
  <div class="map-card">Hi, we're Brindolux</div>
  <svg class="map-pin" width="22" height="32" viewBox="0 0 22 32"><path d="M11 31C4 20 1 15 1 11a10 10 0 0 1 20 0c0 4-3 9-10 20z" fill="#d6392b"/><circle cx="11" cy="11" r="3.5" fill="#7a1a12"/></svg>
</section>

<section class="cta">
  <p>Call us Today for Instant Tech Support NOW!</p>
  <a href="#">CONTACT NOW</a>
</section>

<footer class="site-footer">
  <div class="footer-main">
    <div class="footer-info">
      <div class="footer-col"><h4>Quick Links</h4><ul><li>Home</li><li>Services</li><li>Pricing</li><li>About Us</li><li>Contact Us</li></ul></div>
      <div class="footer-col"><h4>Head Office Address</h4><p>Brindolux Computer Limited<br>Level 4, Quayside House<br>58 Wharf Lane<br>Harbourside Central<br>Harbourside 4720, New Zealand</p><p style="margin-top:10px">NZ Phone: +64 9 555 0184</p></div>
      <div class="footer-col"><h4>Phone</h4><p>USA: +1 555 014 2270<br>UK: +44 20 7946 0318<br>Australia: +61 2 5550 1946</p></div>
      <div class="footer-col"><h4>Phone</h4><p><span class="accent">For Query</span> : info@brindolux.com<br><span class="accent">For Billing</span> : billing@brindolux.com<br><span class="accent">For Support</span> : support@brindolux.com</p></div>
      <div class="footer-base">
        <p class="copyright">COPYRIGHT ©2015 BRINDOLUX COMPUTER SOLUTION. ALL RIGHTS RESERVED.</p>
        <div class="cards"><i></i><i></i><i></i><i></i><i></i></div>
      </div>
    </div>
    <div class="signup">
      <span>FIRST NAME</span><span>LAST NAME</span>
      <span>EMAIL</span><span>PHONE</span>
      <span>COUNTRY</span><span>STATE</span>
      <span>CITY</span><span>ZIP CODE</span>
      <span class="wide">ADDRESS</span>
      <span class="msg">MESSAGE</span>
      <span class="note">Fields marked are required for registration.</span>
      <span class="reg">REGISTER</span>
    </div>
  </div>
</footer>

</body>
</html>
```